Website Banner

I need a website banner for my webpage
Size 950 pixels wide x 284 high
Name of Business: Tamsin's Ledgers
Bookkeeping, Registered BAS Agent and QVTL Certified consultant.
I would like to use the color purple and Aqua - please refer to the QVTL website for ideas. I would like my phone number to be on the banner is possible
0498715203
I have attached a few photos that could be used
Reason: Thanks for the great designs so far - would like to extend for a few more days to see what else comes through.

```html
<!DOCTYPE html>
<html lang="en">
<head>
<meta charset="utf-8">
<title>Tamsin's Ledgers – Website Banner</title>
<link rel="stylesheet" href="https://fonts.googleapis.com/css2?family=Open+Sans:wght@400;600;700&family=Arimo:ital,wght@0,700;1,700&display=swap">
<style>
  :root {
    --purple-deep: #4f1a72;
    --purple-mid: #6a2a91;
    --purple-bright: #8a44b3;
    --purple-band: #5c2080;
    --lilac-text: #e6c9f3;
    --lilac-soft: #d9b8ec;
    --white: #ffffff;
    --photo-dark: #2f2446;
    --photo-mid: #4a3b66;
    --photo-light: #b8a9c2;
  }
  html, body {
    margin: 0;
    padding: 0;
    width: 1200px;
    height: 313px;
    overflow: hidden;
    background: var(--purple-mid);
  }
  .banner {
    position: relative;
    width: 1200px;
    height: 313px;
    overflow: hidden;
    font-family: "Open Sans", Arial, sans-serif;
  }
  .banner__backdrop {
    position: absolute;
    inset: 0;
    width: 1200px;
    height: 313px;
  }
  .brand-name {
    position: absolute;
    left: 58px;
    top: 8px;
    margin: 0;
    font-size: 66px;
    line-height: 1.2;
    color: var(--white);
    white-space: nowrap;
    letter-spacing: -0.5px;
  }
  .brand-name__first { font-weight: 700; }
  .brand-name__second { font-weight: 400; }
  .services {
    position: absolute;
    left: 80px;
    top: 116px;
    width: 580px;
    margin: 0;
    text-align: center;
    font-size: 25px;
    font-weight: 600;
    line-height: 40px;
    color: var(--lilac-text);
  }
  .contact {
    position: absolute;
    left: 88px;
    top: 258px;
    display: flex;
    align-items: center;
    height: 50px;
  }
  .contact__label {
    font-family: "Arimo", Arial, sans-serif;
    font-weight: 700;
    font-size: 27px;
    color: var(--lilac-soft);
    margin-right: 34px;
  }
  .contact__icon {
    width: 30px;
    height: 48px;
    margin-right: 8px;
  }
  .contact__number {
    font-family: "Arimo", Arial, sans-serif;
    font-weight: 400;
    font-size: 37px;
    color: var(--white);
    letter-spacing: 0.5px;
  }
</style>
</head>
<body>
<div class="banner">
  <svg class="banner__backdrop" viewBox="0 0 1200 313" xmlns="http://www.w3.org/2000/svg" aria-hidden="false">
    <defs>
      <linearGradient id="bg-fill" x1="0" y1="0" x2="1" y2="0">
        <stop offset="0" stop-color="#5a1f80"/>
        <stop offset="0.45" stop-color="#7a37a4"/>
        <stop offset="1" stop-color="#63278a"/>
      </linearGradient>
      <radialGradient id="bg-glow" cx="0.32" cy="0.45" r="0.45">
        <stop offset="0" stop-color="#9a55c4" stop-opacity="0.55"/>
        <stop offset="1" stop-color="#9a55c4" stop-opacity="0"/>
      </radialGradient>
      <linearGradient id="photo-fill" x1="0" y1="0" x2="1" y2="0">
        <stop offset="0" stop-color="#3a2a55" stop-opacity="0"/>
        <stop offset="0.18" stop-color="#2f2446" stop-opacity="0.9"/>
        <stop offset="0.45" stop-color="#4a3b66"/>
        <stop offset="0.75" stop-color="#2c2340"/>
        <stop offset="1" stop-color="#b8a9c2"/>
      </linearGradient>
      <linearGradient id="band-fill" x1="0" y1="0" x2="1" y2="0">
        <stop offset="0" stop-color="#561c7a"/>
        <stop offset="0.5" stop-color="#6e2e98"/>
        <stop offset="1" stop-color="#7c3aa6"/>
      </linearGradient>
    </defs>
    <rect width="1200" height="313" fill="url(#bg-fill)"/>
    <rect width="1200" height="313" fill="url(#bg-glow)"/>
    <path role="img" aria-label="Photo of an award presentation: a glass trophy on a stage and two people holding a framed certificate"
          d="M690 0 H1200 V212 C1020 222 860 236 690 248 Z" fill="url(#photo-fill)"/>
    <path d="M0 262 C320 252 820 232 1200 208 V313 H0 Z" fill="url(#band-fill)"/>
    <path d="M0 262 C320 252 820 232 1200 208" fill="none" stroke="#ffffff" stroke-width="3"/>
  </svg>

  <h1 class="brand-name"><span class="brand-name__first">Tamsin's</span> <span class="brand-name__second">Ledgers</span></h1>

  <p class="services">Bookkeeping, Registered BAS Agent and<br>QVTL Certified consultant.</p>

  <div class="contact">
    <span class="contact__label">Contact us:</span>
    <svg class="contact__icon" viewBox="0 0 30 48" xmlns="http://www.w3.org/2000/svg" aria-hidden="true">
      <rect x="4" y="2" width="22" height="44" rx="4" fill="#b06ad8" transform="rotate(12 15 24)"/>
      <rect x="7" y="8" width="16" height="28" rx="1" fill="#3d1358" transform="rotate(12 15 24)"/>
      <circle cx="12" cy="41" r="2" fill="#e6c9f3"/>
    </svg>
    <span class="contact__number">0498715203</span>
  </div>
</div>
</body>
</html>
```